Bref créative
Business Cards & Letterhead for a business that owns franchises
HARTWELL HOLDINGS GROUP
Professional
Gregory T. Pennock, Sr.
President & Co-Owner
3852 Fernhollow Bend, SE
Atlanta, GA
Gregory@HartHoldingsGroup.example
www.hartholdingsgroup.example
Our Logo? Be Creative!!
HARTWELL HOLDINGS GROUP LOGO

```html
<!DOCTYPE html>
<html lang="en">
<head>
<meta charset="utf-8">
<title>Hartwell Holdings Group — Business Cards</title>
<link href="https://fonts.googleapis.com/css2?family=Cinzel:wght@500&family=Open+Sans:wght@400;600&display=swap" rel="stylesheet">
<style>
  :root{
    --bg:#e9e7e3;
    --card:#ffffff;
    --red:#d3252c;
    --red-dark:#a8141b;
    --grey:#8b8d90;
    --grey-light:#c9cacc;
    --ink:#55585c;
  }
  html,body{margin:0;padding:0;overflow:hidden;}
  body{width:1200px;height:629px;background:var(--bg);position:relative;font-family:"Open Sans",sans-serif;}
  .card{position:absolute;width:520px;height:297px;background:var(--card);box-shadow:0 6px 18px rgba(0,0,0,.18);overflow:hidden;}
  .card--front{left:50px;top:166px;}
  .card--back{left:630px;top:166px;}
  .brand{display:flex;align-items:center;gap:14px;}
  .brand__dot{width:54px;height:54px;border-radius:50%;background:var(--red);flex:none;}
  .brand__name{font-family:"Cinzel",serif;font-weight:500;color:var(--grey);line-height:1.15;letter-spacing:2px;}
  .card--front .brand{position:absolute;left:120px;top:112px;}
  .card--front .brand__name{font-size:25px;}
  .card--back .brand{position:absolute;left:36px;top:112px;}
  .card--back .brand__dot{width:44px;height:44px;}
  .card--back .brand__name{font-size:20px;}
  .swoosh{position:absolute;left:0;top:0;}
  .holder{position:absolute;right:22px;top:22px;text-align:right;color:#fff;}
  .holder__name{font-size:11px;font-weight:600;}
  .holder__title{font-size:9px;}
  .contacts{position:absolute;left:36px;bottom:22px;margin:0;padding:0;list-style:none;}
  .contacts li{display:flex;align-items:center;gap:8px;font-size:9px;color:var(--ink);margin-top:4px;}
  .contacts svg{flex:none;}
</style>
</head>
<body>
  <section class="card card--front">
    <div class="brand">
      <span class="brand__dot"></span>
      <span class="brand__name">HARTWELL<br>HOLDINGS GROUP</span>
    </div>
  </section>

  <section class="card card--back">
    <svg class="swoosh" width="520" height="297" viewBox="0 0 520 297">
      <path d="M150 0 H520 V150 C440 70 310 40 150 0 Z" fill="var(--red)"/>
      <path d="M0 95 C120 40 330 40 520 150 V160 C330 60 140 58 0 105 Z" fill="var(--grey-light)"/>
    </svg>
    <div class="holder">
      <div class="holder__name">Gregory T. Pennock, Sr.</div>
      <div class="holder__title">President &amp; Co-Owner</div>
    </div>
    <div class="brand">
      <span class="brand__dot"></span>
      <span class="brand__name">HARTWELL<br>HOLDINGS GROUP</span>
    </div>
    <ul class="contacts">
      <li><svg width="10" height="10" viewBox="0 0 10 10"><path d="M5 0a3.5 3.5 0 0 1 3.5 3.5C8.5 6 5 10 5 10S1.5 6 1.5 3.5A3.5 3.5 0 0 1 5 0z" fill="var(--red)"/></svg>3852 Fernhollow Bend, SE Atlanta, GA</li>
      <li><svg width="10" height="10" viewBox="0 0 10 10"><rect x="2" y="0" width="6" height="10" rx="1.2" fill="var(--red)"/></svg>(404) 555-0148</li>
      <li><svg width="10" height="10" viewBox="0 0 10 10"><rect x="0" y="3" width="10" height="6" fill="var(--red)"/><rect x="2" y="0" width="6" height="3" fill="var(--red)"/></svg>(404) 555-0172</li>
      <li><svg width="10" height="10" viewBox="0 0 10 10"><rect x="0" y="2" width="10" height="7" fill="var(--red)"/><path d="M0 2l5 4 5-4" stroke="#fff" fill="none"/></svg>Gregory@HartHoldingsGroup.example</li>
      <li><svg width="10" height="10" viewBox="0 0 10 10"><circle cx="5" cy="5" r="4.5" fill="var(--red)"/></svg>www.hartholdingsgroup.example</li>
    </ul>
  </section>
</body>
</html>
```